Brighter Than Dawn Home Entertainment

We are a home theater installation company focus on front projection system and home theater surround system. We built highend home theater for people to enjoy movie, sports and gaming on big screen at home.
I'm looking for a dispaly to showcase our work as well as help people build their home theater

Number of Pages Required

3 page

Colors

Designer to choose colors to be used in the design.

Requirements
Must have
• Home Page
• What we do
• Who we are
• Gallery
• Contact Us
Nice to have
• Picture jump out of big screen make a 3D feeling

```html
<!DOCTYPE html>
<html lang="en">
<head>
<meta charset="UTF-8">
<title>Brighter Than Dawn Home Entertainment — Gallery</title>
<link rel="stylesheet" href="https://fonts.googleapis.com/css2?family=Hind:wght@400;600&display=swap">
<style>
  :root {
    --ink: #000000;
    --paper: #ffffff;
    --text-dark: #111111;
    --accent-yellow: #f5c518;
    --product-dark: #1c1c1e;
    --product-mid: #3a3a3d;
  }
  html, body {
    margin: 0;
    padding: 0;
    width: 911px;
    height: 1200px;
    overflow: hidden;
    background: var(--ink);
  }
  .page {
    position: relative;
    width: 911px;
    height: 1200px;
    font-family: "Hind", Arial, sans-serif;
  }
  .section {
    position: absolute;
    left: 0;
    width: 911px;
  }
  .section--hero { top: 0; height: 473px; background: var(--ink); }
  .section--echo { top: 473px; height: 370px; background: var(--paper); }
  .section--k9 { top: 843px; height: 357px; background: var(--ink); }

  .brand {
    position: absolute;
    left: 58px;
    top: 26px;
    margin: 0;
    font-size: 38px;
    font-weight: 600;
    line-height: 1;
    color: var(--paper);
  }
  .nav a {
    position: absolute;
    top: 36px;
    font-size: 14.5px;
    color: var(--paper);
    text-decoration: none;
  }
  .nav .nav__home { left: 479px; }
  .nav .nav__gallery { left: 634px; }
  .nav .nav__gallery::after {
    content: "";
    position: absolute;
    left: 0;
    right: 0;
    bottom: -2px;
    height: 2px;
    background: var(--accent-yellow);
  }
  .nav .nav__contact { left: 794px; }

  .product-title {
    position: absolute;
    margin: 0;
    line-height: 1;
    font-weight: 600;
    white-space: nowrap;
  }
  .product-title--volta { left: 38px; top: 118px; font-size: 84px; color: var(--paper); }
  .product-title--echo { left: 555px; top: 22px; font-size: 62px; color: var(--text-dark); }
  .product-title--k9 { left: 40px; top: 62px; font-size: 84px; color: var(--paper); }

  .blurb {
    position: absolute;
    width: 314px;
    margin: 0;
    font-size: 10.2px;
    line-height: 13.7px;
    text-align: justify;
    text-align-last: justify;
  }
  .section--hero .blurb { left: 37px; top: 229px; color: var(--paper); }
  .section--echo .blurb { left: 551px; top: 127px; color: var(--text-dark); }
  .section--k9 .blurb { left: 37px; top: 164px; color: var(--paper); }

  .quote-button {
    position: absolute;
    width: 142px;
    height: 38px;
    box-sizing: border-box;
    border: 2px solid var(--accent-yellow);
    border-radius: 19px;
    display: flex;
    align-items: center;
    justify-content: center;
    font-size: 15.5px;
    text-decoration: none;
  }
  .section--hero .quote-button { left: 97px; top: 371px; color: var(--paper); }
  .section--echo .quote-button { left: 639px; top: 269px; color: var(--text-dark); }
  .section--k9 .quote-button { left: 97px; top: 306px; color: var(--paper); }

  .product-photo { position: absolute; }
  .product-photo--hero {
    left: 457px; top: 123px; width: 350px; height: 276px;
    background: radial-gradient(ellipse at 60% 60%, var(--product-mid), var(--product-dark) 55%, var(--ink) 80%);
  }
  .product-photo--echo {
    left: 66px; top: 8px; width: 440px; height: 342px;
    background: radial-gradient(ellipse at 55% 60%, var(--product-mid), var(--product-dark) 50%, #f2f2f2 82%);
  }
  .product-photo--k9 {
    left: 593px; top: 149px; width: 234px; height: 189px;
    background: linear-gradient(135deg, var(--product-mid), var(--product-dark) 60%, #0d0d0d);
  }
</style>
</head>
<body>
<div class="page">

  <section class="section section--hero">
    <h1 class="brand">BTD</h1>
    <nav class="nav">
      <a class="nav__home" href="#">Home</a>
      <a class="nav__gallery" href="#">Gallery</a>
      <a class="nav__contact" href="#">Contact Us</a>
    </nav>
    <h2 class="product-title product-title--volta">VOLTA</h2>
    <p class="blurb">We are the leading Home Theater Company&nbsp; Lorem Ipsum get<br>tridiot Lorem Ipsum get tridiot We are the leading Home Theater<br>Company&nbsp; Lorem Ipsum get tridiot Lorem Ipsum get tridiotWe are<br>the leading Home Theater Company&nbsp; Lorem Ipsum get tridiot<br>Lorem Ipsum get tridiotWe are the leading Home Theater<br>Company&nbsp; Lorem Ipsum get tridiot Lorem Ipsum get t tridiot</p>
    <a class="quote-button" href="#">Get Quote</a>
    <div class="product-photo product-photo--hero" role="img" aria-label="Black home theater surround system with tall tower speakers, subwoofer and center unit"></div>
  </section>

  <section class="section section--echo">
    <div class="product-photo product-photo--echo" role="img" aria-label="Black home theater speaker set with tower speakers, subwoofer and player on white"></div>
    <h2 class="product-title product-title--echo">ECHO ONE</h2>
    <p class="blurb">We are the leading Home Theater Company&nbsp; Lorem Ipsum get<br>tridiot Lorem Ipsum get tridiot We are the leading Home Theater<br>Company&nbsp; Lorem Ipsum get tridiot Lorem Ipsum get tridiotWe are<br>the leading Home Theater Company&nbsp; Lorem Ipsum get tridiot<br>Lorem Ipsum get tridiotWe are the leading Home Theater<br>Company&nbsp; Lorem Ipsum get tridiot Lorem Ipsum get t tridiot</p>
    <a class="quote-button" href="#">Get Quote</a>
  </section>

  <section class="section section--k9">
    <h2 class="product-title product-title--k9">K9</h2>
    <p class="blurb">We are the leading Home Theater Company&nbsp; Lorem Ipsum get<br>tridiot Lorem Ipsum get tridiot We are the leading Home Theater<br>Company&nbsp; Lorem Ipsum get tridiot Lorem Ipsum get tridiotWe are<br>the leading Home Theater Company&nbsp; Lorem Ipsum get tridiot<br>Lorem Ipsum get tridiotWe are the leading Home Theater<br>Company&nbsp; Lorem Ipsum get tridiot Lorem Ipsum get t tridiot</p>
    <a class="quote-button" href="#">Get Quote</a>
    <div class="product-photo product-photo--k9" role="img" aria-label="Close view of a black subwoofer with a small speaker beside it"></div>
  </section>

</div>
</body>
</html>
```